Banner photo design to use for our marketing products

We need a banner photo for landing page of our website and to use in our other marketing products. We need it to reflect the idea of that "we are drowning in data but starving for information". Our company is a software- internet of things company that creates products to help companies have meaningful insights from their big and complicated data. We like simple designs, which reflects just our concerns and no more than that. Here is our website www.corvanteq.com. When you click on the link, you will see blue pictures in the landing page. Basically, we want to replace it/them with the new design. The text you will see on the banner is added by us later on, so you do not need to add the text to your designs as it is better for us if the text is changeable.
Target Market(s)
Software company customers, decision makers of all industries that is actively working with data.
Industry/Entity Type
Software
Requirements
Must have
- Our project should reflect the idea of creating meanings from huge and complicated data. It must arouse curiosity for customers feeling stuck in huge data to dig deeper in our website.
Nice to have
- It may have an idea to say how can our company can change the way things go traditionally. In our current landing page, you will see a mountain and then a diamond. Idea was, there are mountains of data but we know how to dig into your information diamonds. New design can also stay on this track or could be more creative.. We not only help collecting meaningful data but also visualize them. So it may nice to have it.
Should not have
- We do not like indirect messages and full-colored designs. We want to reflect the way of Nordic companies marketing, which is simple and direct.

```html
<!DOCTYPE html>
<html lang="en">
<head>
<meta charset="UTF-8">
<title>Corvanteq — Landing Banner</title>
<link rel="stylesheet" href="https://fonts.googleapis.com/css2?family=Bebas+Neue&display=swap">
<style>
  :root {
    --violet-deep: #3d1670;
    --violet: #4f1a86;
    --violet-soft: #3a2480;
    --card-top: #2c3579;
    --card-bottom: #1a1d52;
    --ink: #ffffff;
    --ink-soft: rgba(255, 255, 255, 0.88);
    --teal: #5ff0e0;
    --teal-mid: #3fc6cf;
    --teal-dark: #3a5fb0;
    --cta-start: #e89763;
    --cta-end: #e0577f;
  }
  * { box-sizing: border-box; margin: 0; padding: 0; }
  html, body {
    width: 1200px;
    height: 960px;
    overflow: hidden;
  }
  body {
    background: linear-gradient(100deg, var(--violet) 0%, var(--violet-deep) 45%, var(--violet-soft) 100%);
    font-family: "Bebas Neue", "Arial Narrow", sans-serif;
    color: var(--ink);
    position: relative;
  }
  .hero-card {
    position: absolute;
    left: 140px;
    top: 130px;
    width: 920px;
    height: 660px;
    border-radius: 18px;
    background: linear-gradient(160deg, var(--card-top) 0%, #222763 50%, var(--card-bottom) 100%);
    box-shadow: 0 20px 50px rgba(10, 6, 40, 0.45);
    overflow: hidden;
  }
  .hero-card__backdrop {
    position: absolute;
    inset: 0;
    background:
      radial-gradient(ellipse at 55% 70%, rgba(20, 18, 60, 0.55) 0%, rgba(20, 18, 60, 0) 60%),
      linear-gradient(135deg, rgba(60, 80, 160, 0.18) 0%, rgba(20, 20, 70, 0) 55%);
  }
  .hero-card__facet {
    position: absolute;
    inset: 0;
    width: 100%;
    height: 100%;
  }
  .headline {
    position: absolute;
    left: 40px;
    top: 90px;
    font-size: 50px;
    line-height: 1.12;
    letter-spacing: 0.5px;
    font-weight: 400;
  }
  .subline {
    position: absolute;
    left: 40px;
    top: 290px;
    font-size: 28px;
    letter-spacing: 0.5px;
    font-weight: 400;
  }
  .cta {
    position: absolute;
    left: 40px;
    top: 382px;
    width: 136px;
    height: 46px;
    border-radius: 23px;
    background: linear-gradient(90deg, var(--cta-start), var(--cta-end));
    font-size: 21px;
    letter-spacing: 0.5px;
    display: flex;
    align-items: center;
    justify-content: center;
    color: var(--ink);
  }
  .social-links {
    position: absolute;
    left: 62px;
    top: 520px;
    display: flex;
    gap: 6px;
  }
  .social-links__item {
    width: 16px;
    height: 16px;
    border: 1.5px solid var(--ink);
    border-radius: 3px;
  }
  .server-illustration {
    position: absolute;
    left: 620px;
    top: 100px;
    width: 140px;
    height: 280px;
    border-radius: 16px;
    background: linear-gradient(180deg, var(--teal) 0%, var(--teal-mid) 55%, var(--teal-dark) 100%);
    box-shadow: 0 18px 40px rgba(10, 10, 50, 0.45);
  }
  .brand {
    position: absolute;
    right: 70px;
    bottom: 34px;
    font-size: 28px;
    letter-spacing: 1.5px;
    color: var(--ink-soft);
    font-weight: 400;
  }
</style>
</head>
<body>
  <section class="hero-card">
    <div class="hero-card__backdrop" role="img" aria-label="Dim office interior with desk and chairs, tinted deep blue"></div>
    <svg class="hero-card__facet" viewBox="0 0 920 660" preserveAspectRatio="none" aria-hidden="true">
      <polygon points="520,120 880,0 920,520 700,600" fill="#2a3a8a" opacity="0.25"/>
      <polygon points="200,400 420,290 560,530 260,660" fill="#141a4a" opacity="0.35"/>
    </svg>

    <h1 class="headline">The world is drowning<br>in data but starving<br>for information</h1>
    <p class="subline">Our customers are not</p>
    <a class="cta">Here is why</a>

    <div class="social-links">
      <span class="social-links__item"></span>
      <span class="social-links__item"></span>
      <span class="social-links__item"></span>
    </div>

    <div class="server-illustration" role="img" aria-label="Isometric stack of five glowing teal data servers, raw data turning into insight"></div>

    <div class="brand">Corvanteq</div>
  </section>
</body>
</html>
```